Redesign existing website

We would like a redesign of the website http://www.velbrisanalytics.com that creates a more modern, up to date look.

Velbris Analytics creates software for social science research and is focused on making the software user friendly and easy to use. We would like to convey seriousness, but also
a very up to date, just released look.

Feel free to modify the logo if you wish.

Target Market(s)

Academics, researchers

Industry/Entity Type

Software

Requirements
Must have
• The design should incorporate the same information as the current website.

```html
<!DOCTYPE html>
<html lang="en">
<head>
<meta charset="utf-8">
<title>Velbris Analytics</title>
<link href="https://fonts.googleapis.com/css2?family=Arimo:ital,wght@0,400;0,700;1,400&display=swap" rel="stylesheet">
<style>
  :root {
    --page-bg: #d7d7d7;
    --navy: #1f3a93;
    --text-gray: #6b6b6b;
    --tagline-gray: #5a5a5a;
    --bar-top: #7a7a7a;
    --bar-bottom: #3e3e3e;
    --bar-active: #2a2a2a;
    --divider: #8c8c8c;
    --white: #ffffff;
    --panel-bg: #d3d3d3;
    --hero-top: #a9c3de;
    --hero-bottom: #b7bfb3;
  }
  * { margin: 0; padding: 0; box-sizing: border-box; }
  html, body { width: 1200px; height: 1011px; overflow: hidden; }
  body {
    position: relative;
    background: var(--page-bg);
    font-family: "Arimo", Arial, sans-serif;
  }
  .brand {
    position: absolute; left: 23px; top: 20px; width: 220px; height: 130px;
  }
  .brand-dot {
    position: absolute; left: 86px; top: 0; width: 88px; height: 88px;
    border-radius: 50%; background: var(--navy);
  }
  .brand-name {
    position: absolute; left: 0; top: 98px; width: 260px;
    font-size: 25px; color: var(--navy); white-space: nowrap;
  }
  .tagline {
    position: absolute; left: 774px; top: 79px; width: 410px;
    font-size: 24px; font-style: italic; line-height: 38px;
    color: var(--tagline-gray); white-space: nowrap;
  }
  .main-nav {
    position: absolute; left: 19px; top: 171px; width: 1158px; height: 58px;
    border-radius: 10px; overflow: hidden;
    background: linear-gradient(var(--bar-top), var(--bar-bottom));
  }
  .nav-item {
    position: absolute; top: 0; height: 58px; line-height: 58px;
    color: var(--white); font-size: 18px; text-align: center;
  }
  .nav-item.is-active { background: var(--bar-active); }
  .nav-divider {
    position: absolute; top: 6px; width: 1px; height: 46px; background: var(--divider);
  }
  .account-link {
    position: absolute; left: 979px; top: 12px; width: 163px; height: 33px;
    border: 1px solid #9a9a9a; border-radius: 8px;
    color: var(--white); font-size: 18px; line-height: 31px; text-align: center;
  }
  .hero {
    position: absolute; left: 23px; top: 237px; width: 1152px; height: 345px;
    border: 3px solid #f2f2f2; border-radius: 10px; overflow: hidden;
    background: linear-gradient(var(--hero-top), var(--hero-bottom));
  }
  .hero-dots {
    position: absolute; left: 566px; top: 560px; height: 14px; display: flex; gap: 10px;
  }
  .hero-dot { width: 13px; height: 13px; border-radius: 50%; background: #f4f4f4; }
  .hero-dot.is-current { background: #111; }
  .intro-heading {
    position: absolute; left: 22px; top: 601px;
    font-size: 33px; color: var(--navy); font-weight: 400;
  }
  .intro-rule {
    position: absolute; left: 23px; top: 642px; width: 640px; height: 2px;
    background: linear-gradient(90deg, var(--navy), rgba(31,58,147,0));
  }
  .intro-text {
    position: absolute; left: 23px; top: 678px; width: 620px;
    font-size: 20px; line-height: 31px; color: var(--text-gray);
  }
  .intro-text p + p { margin-top: 16px; }
  .preview-card {
    position: absolute; left: 802px; top: 650px; width: 290px; height: 199px;
    background: var(--panel-bg); border: 1px solid #c0c0c0; border-radius: 8px;
    box-shadow: 0 2px 8px rgba(0,0,0,0.3);
    text-align: center; font-style: italic; padding-top: 24px;
  }
  .preview-note { font-size: 21px; color: var(--navy); }
  .preview-product { font-size: 30px; line-height: 38px; color: var(--text-gray); margin-top: 10px; }
  .preview-download { font-size: 21px; color: var(--navy); margin-top: 4px; }
  .site-footer {
    position: absolute; left: 19px; top: 952px; width: 1158px; height: 70px;
    border-radius: 10px;
    background: linear-gradient(var(--bar-top), var(--bar-bottom));
    color: var(--white); font-size: 15px; text-align: center; padding-top: 20px;
  }
</style>
</head>
<body>
  <header>
    <div class="brand">
      <span class="brand-dot"></span>
      <span class="brand-name">Velbris Analytics</span>
    </div>
    <p class="tagline">Increasing the power and efficiency of<br>empirical social science research</p>
  </header>

  <nav class="main-nav">
    <span class="nav-item is-active" style="left:0;width:143px;">Home</span>
    <span class="nav-item" style="left:143px;width:135px;">Project</span>
    <span class="nav-divider" style="left:278px;"></span>
    <span class="nav-item" style="left:279px;width:126px;">News</span>
    <span class="nav-divider" style="left:405px;"></span>
    <span class="nav-item" style="left:406px;width:135px;">About us</span>
    <span class="nav-divider" style="left:541px;"></span>
    <span class="nav-item" style="left:542px;width:144px;">Contact us</span>
    <span class="nav-divider" style="left:686px;"></span>
    <span class="account-link">Login | Register</span>
  </nav>

  <div class="hero" role="img" aria-label="Banner photo of an open road through green hills under a cloudy blue sky"></div>
  <div class="hero-dots">
    <span class="hero-dot"></span>
    <span class="hero-dot is-current"></span>
    <span class="hero-dot"></span>
    <span class="hero-dot"></span>
  </div>

  <main>
    <h1 class="intro-heading">Empowering the social science researcher</h1>
    <div class="intro-rule"></div>
    <div class="intro-text">
      <p>The mission of Velbris Analytics, Inc. is to produce software products that multiply the power and efficiency of empirical scientific research in the social sciences.</p>
      <p>A central goal is to expand access to complex data sources and to the advanced methods of scientific investigation needed to analyze them.</p>
    </div>
    <aside class="preview-card">
      <p class="preview-note">Preview Release Available!</p>
      <p class="preview-product">Velbris Data<br>Manager</p>
      <p class="preview-download">Download Preview</p>
    </aside>
  </main>

  <footer class="site-footer">Copyright © 2011 velbrisanalytics.com</footer>
</body>
</html>
```